R T Security Flyer - Security Based Company

Security company offering installation of CCTV and Intruder alarm systems mainly but not limited to home alarms. Feel free to be creative

Target Market(s)

Residential and Commercial properties, Facility Managers, local business

Requirements
Must have
• smart professional finish, logo and latest up to date pictures if on kit

```html
<!DOCTYPE html>
<html lang="en">
<head>
<meta charset="utf-8">
<title>R T Security Flyer</title>
<link rel="stylesheet" href="https://fonts.googleapis.com/css2?family=Exo+2:wght@400;500&family=Oswald:wght@500&family=Playfair+Display:ital,wght@1,500&display=swap">
<style>
  :root {
    --backdrop: #fbe3c9;
    --charcoal: #2b2b2d;
    --ink: #0b0b0c;
    --orange: #e8512a;
    --orange-soft: #f05a2e;
    --white: #ffffff;
    --grey-text: #d9d9d9;
    --frame-blue: #3b57c9;
  }
  * { margin: 0; padding: 0; box-sizing: border-box; }
  html, body { width: 1200px; height: 848px; overflow: hidden; }
  body { background: var(--backdrop); position: relative; font-family: "Exo 2", sans-serif; }

  .page { position: absolute; overflow: hidden; }

  /* Front */
  .front { left: 80px; top: 74px; width: 493px; height: 700px;
    background: radial-gradient(ellipse at 55% 40%, #3a3a3c 0%, var(--charcoal) 60%, #232325 100%); }
  .brand { position: absolute; left: 48px; top: 44px; width: 110px; text-align: center; }
  .brand-mark { width: 26px; height: 26px; border: 3px solid var(--orange); margin: 0 auto 8px; }
  .brand-name { font-family: "Exo 2", sans-serif; font-weight: 500; font-size: 15px; color: var(--orange); letter-spacing: 0.5px; text-transform: uppercase; white-space: nowrap; }
  .camera-photo { position: absolute; left: 124px; top: 70px; width: 196px; height: 284px;
    border-radius: 40px 40px 90px 90px;
    background: radial-gradient(ellipse at 50% 45%, #e9eaec 0%, #bfc2c6 55%, rgba(60,60,62,0) 80%); }
  .headline { position: absolute; left: 188px; top: 390px; font-family: "Playfair Display", serif; font-style: italic; font-weight: 500; font-size: 24px; line-height: 30px; color: var(--grey-text); }
  .headline .accent { color: var(--orange); }
  .cta-band { position: absolute; left: 0; top: 577px; width: 100%; height: 56px; background: var(--orange);
    display: flex; align-items: center; justify-content: center; text-align: center;
    font-family: "Oswald", sans-serif; font-weight: 500; font-size: 12.5px; line-height: 16px; color: var(--white); }
  .partner-band { position: absolute; left: 0; top: 633px; width: 100%; height: 42px; background: var(--white);
    display: flex; align-items: center; justify-content: center; gap: 70px; }
  .partner { display: flex; align-items: center; gap: 6px; font-weight: 500; font-size: 14px; color: #555; }
  .partner-dot { width: 12px; height: 12px; border-radius: 50%; background: #9aa3ad; }

  /* Back */
  .back { left: 628px; top: 76px; width: 492px; height: 696px; background: var(--ink); }
  .siren-photo { position: absolute; left: 44px; top: 44px; width: 116px; height: 140px;
    border-radius: 24px 24px 40px 40px;
    background: radial-gradient(ellipse at 50% 40%, #f4f4f4 0%, #cfcfcf 55%, rgba(20,30,60,0.6) 85%, rgba(0,0,0,0) 100%); }
  .intro-box { position: absolute; left: 217px; top: 48px; width: 257px; height: 120px; border: 1.5px solid var(--frame-blue);
    padding: 12px 12px; font-size: 14.5px; line-height: 18.5px; color: var(--orange-soft); letter-spacing: 0.3px; }
  .benefits-title { position: absolute; left: 0; top: 237px; width: 100%; height: 35px; }
  .benefits-title svg { position: absolute; left: 0; top: 0; }
  .benefits-title span { position: absolute; left: 17px; top: 5px; font-size: 16.5px; color: var(--white); letter-spacing: 0.5px; }
  .benefits { position: absolute; left: 10px; top: 278px; width: 470px; list-style: none; font-size: 11.8px; line-height: 14.7px; color: var(--white); letter-spacing: 0.2px; }
  .benefits li { position: relative; padding-left: 12px; }
  .benefits li::before { content: ""; position: absolute; left: 0; top: 5px; width: 5px; height: 5px; border: 1.2px solid var(--orange); border-radius: 50%; }
  .benefits li + li { margin-top: 10px; }
  .benefits li.spaced { margin-top: 14px; }
  .benefits .note { display: block; margin-left: -12px; }
  .lifestyle-photo { position: absolute; left: 0; top: 572px; width: 100%; height: 124px;
    background: linear-gradient(90deg, #d9dde0 0%, #b9bec2 40%, #7c8289 65%, #c9ccd0 100%); }
  .photo-caption { position: absolute; left: 64px; top: 580px; width: 376px; height: 44px; border-radius: 22px;
    background: rgba(45,45,48,0.82); text-align: center; padding-top: 6px;
    font-family: "Oswald", sans-serif; font-weight: 500; font-size: 11.5px; line-height: 15px; color: var(--white); }
</style>
</head>
<body>

<section class="page front">
  <div class="brand">
    <div class="brand-mark"></div>
    <div class="brand-name">R T Security</div>
  </div>
  <div class="camera-photo" role="img" aria-label="Wall-mounted white dome CCTV camera with a certification badge"></div>
  <h1 class="headline">Are you<br>looking to<br><span class="accent">keep you or your<br>premises safe?</span></h1>
  <div class="cta-band">If you are looking to improve the security in your home, office or commercial<br>property then call a member of our team today for a free quote.</div>
  <div class="partner-band">
    <div class="partner"><span class="partner-dot"></span>TradeTrust</div>
    <div class="partner"><span class="partner-dot"></span>Alarmlink</div>
  </div>
</section>

<section class="page back">
  <div class="siren-photo" role="img" aria-label="White alarm siren box with company name and phone 01632 960 482"></div>
  <div class="intro-box">R T Security Systems are using the latest cloud-based technology to stay connected with your home and business 24/7.</div>
  <div class="benefits-title">
    <svg width="492" height="35" viewBox="0 0 492 35">
      <polygon points="0,0 368,0 382,30 492,30 492,35 0,35" fill="#e8512a"/>
    </svg>
    <span>Some benefits of cloud services are;</span>
  </div>
  <ul class="benefits">
    <li>High level support 24/7</li>
    <li>Reduce engineer call outs and running costs</li>
    <li>Identify issues in advance</li>
    <li>Remotely manage systems to ensure correct operation</li>
    <li>Remote health checks carried out to keep<br>your system performing as it should</li>
    <li class="spaced">Automatically update your system with the latest releases via cloud<br>application software</li>
    <li class="spaced">Interact, control and integrate your security system like never before
      <span class="note">With the new cloud-based system we can check the alarm performance anytime you need it. This gives us the capability to assist you in any of your needs, be that changing user codes or system configuration. We are always there, working in the background to make sure you have the support and help you need. This is taking alarm systems into the future and leaving the stand-alone systems in the past.</span>
    </li>
  </ul>
  <div class="lifestyle-photo" role="img" aria-label="Bright modern home interior with wall-mounted alarm keypads"></div>
  <div class="photo-caption">R T Security Systems are always there,<br>always available, wherever and whenever you need us.</div>
</section>

</body>
</html>
```